Business Card Design, including supply of raw art files plus a vector diagram of the zelvon logo and

We need the business card design for a company that is launching a new exciting product. The brief requires the submission of the following once the final design is chosen:

- business card layout including raw files
- a composite vector image file of the zelvon logo and tag line
- a standalone vector image file of the zelvon logo

The product will be launched as a customer engagement app.

It has 4 core modules which enables a person to do multiple things - book tours and activities, order takeaways, search for local deals and offers. A universal currency is at the heart of this product. When you use the app, you earn cashback rewards when shopping or buying at any of the merchant partners across the modules as . These rewards can then be used as full or part payment when buying goods or services at these merchant partners.

The business card must help us build the brand, communicate the benefit of the brand's key focus - the ability to earn and burn this universal cashback ccurrency - across the 4 modules - booking of tours and activities, ordering, searching for local deals and payment.

We would like the design to use the brand's blue colour the hex colour is: 00
Dark grey : 646464
Darker blue shadow: 058bdd
Main Blue: 0084ff

We need to translate this into a CMYK print or spot colour print.

Both print options to be supplied as separate files.

An example of the base concept we have in mind is attached for your reference.

The font used by the brand is Proxima Nova.

Note: the duration has been set as 2 days.

Industry/Entity Type

Business

Contact Information for Business Card

Carla Mendoza
Marketing
W: www.zelvon.example
M: + 61 400555123
T: +61 2 5550 1473
A: Suite 7, Level 2, 14-18 Harwick Street, Sydney, NSW, 2000, Australia

Font styles to use
Sans Serif

Requirements
Must have
• zelVon logo and tagline
• address details
• zelVon icons as supplied
Nice to have
• would like to have the option of a spot varnish layer over the logo and icons at the back of the card

```html
<!DOCTYPE html>
<html lang="en">
<head>
<meta charset="utf-8">
<title>zelVon business card</title>
<link rel="stylesheet" href="https://fonts.googleapis.com/css2?family=Raleway:wght@200;300&family=Roboto:wght@400;500;700&display=swap">
<style>
  :root {
    --brand-blue: #2b86cc;
    --accent-blue: #1f8be0;
    --ink: #2a2a2a;
    --grey: #646464;
    --paper: #ffffff;
    --backdrop: #3a3330;
  }
  * { box-sizing: border-box; margin: 0; padding: 0; }
  html, body { width: 1200px; height: 900px; overflow: hidden; }
  body {
    background: var(--backdrop);
    font-family: "Roboto", Arial, sans-serif;
    position: relative;
  }
  .card {
    position: absolute;
    width: 520px;
    height: 318px;
    border-radius: 3px;
    box-shadow: 0 14px 30px rgba(0,0,0,.45);
    overflow: hidden;
  }
  /* front */
  .card-front { left: 50px; top: 110px; background: var(--brand-blue); color: var(--paper); }
  .front-brand { position: absolute; left: 92px; top: 88px; display: flex; align-items: center; gap: 18px; }
  .brand-dot { width: 74px; height: 74px; border-radius: 50%; background: var(--paper); flex: none; }
  .front-wordmark { font-family: "Raleway", Arial, sans-serif; font-weight: 200; font-size: 66px; line-height: 1; letter-spacing: 1px; }
  .tagline { position: absolute; left: 184px; top: 168px; font-family: "Raleway", Arial, sans-serif; font-weight: 300; font-size: 22px; letter-spacing: .5px; opacity: .9; white-space: nowrap; }
  .module-icons { position: absolute; left: 120px; top: 222px; display: flex; gap: 30px; }
  .module-icons svg { width: 26px; height: 26px; fill: none; stroke: var(--paper); stroke-width: 2; stroke-linecap: round; stroke-linejoin: round; }

  /* back */
  .card-back { left: 630px; top: 420px; background: var(--paper); color: var(--ink); }
  .holder { position: absolute; left: 30px; top: 34px; padding-left: 12px; border-left: 4px solid var(--accent-blue); }
  .holder-name { font-weight: 700; font-size: 20px; line-height: 1.1; }
  .holder-role { font-size: 12px; color: var(--accent-blue); margin-top: 2px; }
  .back-brand { position: absolute; right: 28px; top: 100px; display: flex; align-items: center; gap: 12px; }
  .back-brand .brand-dot { width: 62px; height: 62px; background: var(--accent-blue); }
  .back-wordmark { font-family: "Raleway", Arial, sans-serif; font-weight: 200; font-size: 54px; line-height: 1; color: var(--grey); }
  .contacts { position: absolute; left: 30px; top: 176px; list-style: none; font-size: 13px; line-height: 19px; white-space: nowrap; }
  .contacts li { display: flex; align-items: center; gap: 7px; }
  .contact-icon { width: 13px; height: 13px; border-radius: 2px; background: var(--accent-blue); display: flex; align-items: center; justify-content: center; flex: none; }
  .contact-icon svg { width: 9px; height: 9px; fill: var(--paper); }
</style>
</head>
<body>

<section class="card card-front" aria-label="Card front">
  <div class="front-brand">
    <span class="brand-dot"></span>
    <span class="front-wordmark">zelVon</span>
  </div>
  <p class="tagline">the reward wallet</p>
  <div class="module-icons">
    <svg viewBox="0 0 24 24" aria-label="Order takeaways"><path d="M5 3l14 18M19 3L5 21"/><path d="M16 3c3 1 3 5 0 6"/></svg>
    <svg viewBox="0 0 24 24" aria-label="Pay"><path d="M5 9a7 7 0 0 1 12-3l2 2M19 15a7 7 0 0 1-12 3l-2-2"/><path d="M19 4v4h-4M5 20v-4h4"/></svg>
    <svg viewBox="0 0 24 24" aria-label="Local deals"><path d="M3 12l9-9h8v8l-9 9z"/><circle cx="16" cy="8" r="1.5"/></svg>
    <svg viewBox="0 0 24 24" aria-label="Tours and activities"><rect x="3" y="7" width="18" height="13" rx="2"/><path d="M8 7l2-3h4l2 3"/><circle cx="12" cy="13" r="3.5"/></svg>
  </div>
</section>

<section class="card card-back" aria-label="Card back">
  <div class="holder">
    <p class="holder-name">Carla Mendoza</p>
    <p class="holder-role">Marketing</p>
  </div>
  <div class="back-brand">
    <span class="brand-dot"></span>
    <span class="back-wordmark">zelVon</span>
  </div>
  <ul class="contacts">
    <li><span class="contact-icon"><svg viewBox="0 0 10 10"><rect x="3" y="1" width="4" height="8" rx="1"/></svg></span>+ 61 400555123</li>
    <li><span class="contact-icon"><svg viewBox="0 0 10 10"><path d="M2 1l2 0 1 2-1 1c.5 1 1 1.5 2 2l1-1 2 1v2c-4 0-7-3-7-7z"/></svg></span>+61 2 5550 1473</li>
    <li><span class="contact-icon"><svg viewBox="0 0 10 10"><rect x="1" y="2" width="8" height="6" rx="1"/></svg></span>www.zelvon.example</li>
    <li><span class="contact-icon"><svg viewBox="0 0 10 10"><path d="M5 1a3 3 0 0 1 3 3c0 2-3 5-3 5S2 6 2 4a3 3 0 0 1 3-3z"/></svg></span>Suite 7, Level 2, 14-18 Harwick Street, Sydney, NSW, 2000, Australia</li>
  </ul>
</section>

</body>
</html>
```